Lumo Tavi Menu Design Project

This project is pretty straight forward. You will be given 3 files which include the following:
1. Our proposed menu
2. Our Company logo
3. A sample menu on what we are looking for design wise

Your job is to create a visually pleasing menu that is simple, clean and fresh. Please refer to our home website for additional information. (www.lumotavi.example) Must be in eps or equivalent format.

Target Market(s)

20s to 40s

Industry/Entity Type

It Company

Requirements
Must have
• Company log
Must be in EPS format

```html
<!DOCTYPE html>
<html lang="en">
<head>
<meta charset="utf-8">
<title>Lumo Tavi Menu</title>
<link rel="stylesheet" href="https://fonts.googleapis.com/css2?family=Arimo:wght@400&family=Tinos:wght@700&family=PT+Sans:wght@400&display=swap">
<style>
  :root {
    --page-bg: #ece8e3;
    --panel-dark: #1a1a1a;
    --panel-mid: #2b2b2b;
    --panel-edge: #111111;
    --heading: #ffffff;
    --dish-name: #ffffff;
    --dish-text: #dcdcdc;
    --brand-faint: rgba(120, 62, 48, 0.32);
  }
  * { box-sizing: border-box; margin: 0; padding: 0; }
  html, body { width: 1200px; height: 534px; overflow: hidden; }
  body { background: var(--page-bg); position: relative; }

  .menu-panel {
    position: absolute;
    top: 55px;
    width: 334px;
    height: 434px;
    border: 1px solid var(--panel-edge);
    overflow: hidden;
    color: var(--dish-text);
  }
  .panel-texture {
    position: absolute; inset: 0;
    background: linear-gradient(90deg, var(--panel-dark) 0%, var(--panel-mid) 45%, var(--panel-dark) 70%, var(--panel-mid) 100%);
  }
  .brand-mark {
    position: absolute;
    left: 0; right: 0; top: 150px;
    text-align: center;
    font-family: "Arimo", sans-serif;
    font-weight: 400;
    font-size: 78px;
    line-height: 0.95;
    letter-spacing: 4px;
    color: var(--brand-faint);
    text-transform: uppercase;
  }
  .section-title {
    position: absolute;
    left: 0; right: 0;
    text-align: center;
    font-family: "Arimo", sans-serif;
    font-weight: 400;
    font-size: 22px;
    letter-spacing: 0.5px;
    color: var(--heading);
  }
  .dish { position: absolute; }
  .dish-name, .dish-price {
    font-family: "Tinos", serif;
    font-weight: 700;
    font-size: 8.3px;
    line-height: 1.25;
    color: var(--dish-name);
    text-align: center;
  }
  .dish-desc {
    margin-top: 4px;
    font-family: "PT Sans", sans-serif;
    font-size: 6.6px;
    line-height: 1.38;
    color: var(--dish-text);
  }
  .dish-desc.centered { text-align: center; }

  .panel-chicken { left: 56px; }
  .panel-seafood { left: 433px; }
  .panel-noodles { left: 810px; }
</style>
</head>
<body>

<section class="menu-panel panel-chicken">
  <div class="panel-texture" role="img" aria-label="Dark brushed wood grain texture"></div>
  <div class="brand-mark">Lumo<br>Tavi</div>

  <h2 class="section-title" style="top:22px;">CHICKEN</h2>

  <div class="dish" style="left:12px; top:62px; width:125px;">
    <p class="dish-name">General Tso's Chicken</p>
    <p class="dish-price">$ 11.75</p>
    <p class="dish-desc">Crispy dark meat chicken with chili peppers in a spicy tangerine sauce topped with scallions.</p>
  </div>
  <div class="dish" style="left:202px; top:62px; width:122px;">
    <p class="dish-name">Chicken Lettuce Cups</p>
    <p class="dish-price">$ 11.75</p>
    <p class="dish-desc">Minced white meat chicken with bell peppers, water chestnuts, black mushrooms, pine nuts, and white crunchies. Served with four lettuce cups.</p>
  </div>
  <div class="dish" style="left:114px; top:128px; width:90px;">
    <p class="dish-name">Moo Goo Gai Pan</p>
    <p class="dish-price">$ 00</p>
  </div>
  <div class="dish" style="left:12px; top:160px; width:125px;">
    <p class="dish-name">Orange Chicken</p>
    <p class="dish-price">$ 11.95</p>
    <p class="dish-desc">Crispy chicken breast with onions and red and green bell peppers in a tangy orange Sauce.</p>
  </div>
  <div class="dish" style="left:202px; top:160px; width:108px;">
    <p class="dish-name">Kung Pao Chicken</p>
    <p class="dish-price">$ 11.95</p>
    <p class="dish-desc">Dark meat chicken with red bell peppers, peanuts and water chestnuts in picy red sauce.</p>
  </div>

  <h2 class="section-title" style="top:221px;">BEEF/PORK</h2>

  <div class="dish" style="left:12px; top:262px; width:125px;">
    <p class="dish-name">Mongolian Beef</p>
    <p class="dish-price">$ 12.25</p>
    <p class="dish-desc">Flank steak, garlic, ginger, and green onions on a bed of white crunchies.</p>
  </div>
  <div class="dish" style="left:202px; top:262px; width:100px;">
    <p class="dish-name">Pepper Steak</p>
    <p class="dish-price">$ 11.95</p>
    <p class="dish-desc">Flank steak, bell peppers onions and garlic in black pepper sauce.</p>
  </div>
  <div class="dish" style="left:114px; top:324px; width:90px;">
    <p class="dish-name">Sweet &amp; Sour Pork</p>
    <p class="dish-price">$ 00</p>
  </div>
  <div class="dish" style="left:12px; top:358px; width:100px;">
    <p class="dish-name">Beef &amp; Broccoli</p>
    <p class="dish-price">$ 11.95</p>
    <p class="dish-desc">Flank steak, broccoli, and black mushrooms sautéed in a garlic brown sauce.</p>
  </div>
  <div class="dish" style="left:202px; top:358px; width:105px;">
    <p class="dish-name">Sliced BBQ Pork</p>
    <p class="dish-price">$ 8.95</p>
    <p class="dish-desc">Tender slices of juicy pork opped with scallions in a barbeque sauce.</p>
  </div>
</section>

<section class="menu-panel panel-seafood">
  <div class="panel-texture" role="img" aria-label="Dark brushed wood grain texture"></div>
  <div class="brand-mark">Lumo<br>Tavi</div>

  <h2 class="section-title" style="top:34px;">SEAFOOD</h2>

  <div class="dish" style="left:11px; top:76px; width:118px;">
    <p class="dish-name">Shrimp w/ Snow Peas</p>
    <p class="dish-price">$ 13.95</p>
    <p class="dish-desc">Large shrimp with snow peas water chestnuts carrots and ginger in a white wine sauce.</p>
  </div>
  <div class="dish" style="left:201px; top:76px; width:100px;">
    <p class="dish-name">Fish w/ ginger soy</p>
    <p class="dish-price">$ 15.95</p>
    <p class="dish-desc">Whole white fish filet steamed with ginger and topped with green onions and cilantro.</p>
  </div>
  <div class="dish" style="left:112px; top:129px; width:94px;">
    <p class="dish-name">Scallops<br>w/ black bean sauce</p>
    <p class="dish-price">$ 00</p>
  </div>
  <div class="dish" style="left:11px; top:165px; width:135px;">
    <p class="dish-name">Kung Pao 3 treasures</p>
    <p class="dish-price">$ 13.95</p>
    <p class="dish-desc">Large shrimp, beef, and chicken beast with scallions, peanuts water chestnuts and chili peppers. Prepared mandarin-Style.</p>
  </div>
  <div class="dish" style="left:201px; top:165px; width:100px;">
    <p class="dish-name">Honey Walnut Shrimp</p>
    <p class="dish-price">$ 13.95</p>
    <p class="dish-desc">Lightly crisped savory shrimp with honey-Glazed walnuts.</p>
  </div>

  <h2 class="section-title" style="top:234px;">VEGETABLES</h2>

  <div class="dish" style="left:11px; top:278px; width:90px;">
    <p class="dish-name">Bak Choy w/ Mushrooms</p>
    <p class="dish-price">$ 6.95</p>
    <p class="dish-desc">Baby bokchoy and black mushrooms sautéed in a brown sauce.</p>
  </div>
  <div class="dish" style="left:201px; top:278px; width:108px;">
    <p class="dish-name">Spicy Garlic Eggplant</p>
    <p class="dish-price">$ 8.95</p>
    <p class="dish-desc">Sautéed chinese eggplant, red onions and scallions in a spicy garlic sauce.</p>
  </div>
  <div class="dish" style="left:122px; top:316px; width:74px;">
    <p class="dish-name">Spinach w/ garlic</p>
    <p class="dish-price">$ 6.95</p>
    <p class="dish-desc centered">Sautéed spinach with garlic.</p>
  </div>
  <div class="dish" style="left:11px; top:349px; width:96px;">
    <p class="dish-name">Schezuan String Bean</p>
    <p class="dish-price">$ 8.95</p>
    <p class="dish-desc">Blue lake green beans and garlic sautéed with pickled szechwan vegetables.</p>
  </div>
  <div class="dish" style="left:201px; top:349px; width:100px;">
    <p class="dish-name">Fragrant Vegetables</p>
    <p class="dish-price">$ 8.95</p>
    <p class="dish-desc">Mixed vegetables with white wine, curry, garlic, black bean kungpao, or vegetarian sauce.</p>
  </div>
</section>

<section class="menu-panel panel-noodles">
  <div class="panel-texture" role="img" aria-label="Dark brushed wood grain texture"></div>
  <div class="brand-mark">Lumo<br>Tavi</div>

  <h2 class="section-title" style="top:20px;">NOODLES</h2>

  <div class="dish" style="left:16px; top:56px; width:122px;">
    <p class="dish-name">Chow Mein</p>
    <p class="dish-price">$ 12.95</p>
    <p class="dish-desc">Crispy egg noodles or soft lo mein noodles with large vegetables and chicken, pork or vegetables. Beef or shrimp instead add $1.00.</p>
  </div>
  <div class="dish" style="left:171px; top:56px; width:122px;">
    <p class="dish-name">Lo Mein</p>
    <p class="dish-price">$ 10.95</p>
    <p class="dish-desc">Soft lo mein noodles with shredded vegetables and chicken, pork, or vegetables.<br>Beef or shrimp instead add $1.00.</p>
  </div>
  <div class="dish" style="left:120px; top:134px; width:84px;">
    <p class="dish-name">Seafood Noodles</p>
    <p class="dish-price">$ 00</p>
  </div>
  <div class="dish" style="left:14px; top:166px; width:128px;">
    <p class="dish-name">Singapore Noodles</p>
    <p class="dish-price">$ 10.95</p>
    <p class="dish-desc">Shrimp, barbeque pork, bean sprouts, onions, egg, and bell peppers with rice noodles in a curry sauce</p>
  </div>
  <div class="dish" style="left:171px; top:166px; width:112px;">
    <p class="dish-name">Pad Thai</p>
    <p class="dish-price">$ 12.95</p>
    <p class="dish-desc">Rice noodles with chicken shrimp eggs, onions, and scallions topped with peanuts and cilantro.</p>
  </div>
</section>

</body>
</html>
```